Book Cover for: TITLE Mend the Quiet Tide SUBTITLE For partners who still choose to stay close

We need a full cover design for a book on relationships written by husband and wife team, Marla and Dennis Holtwick, PhD. This book will offer hope for couples that are on the verge of breaking up but want to work things out and stay together. The theme is to teach couples about their own reactions to their partner, how moods affect a relationship, how to get creative to solving problems and how to have a good feeling towards your partner regardless of differences. This book is about hope. It is a positive look at relationships that feel hopeless.

Target Market(s)

Married or couples that are going through a difficult time and are considering splitting up due to, communication difficulties, addiction, affair. We imagine the book will appeal to women more than men but still want a cover that men would be comfortable picking up.

Colors

Designer to choose colors to be used in the design.

Requirements
Must have
• We want the cover to beautiful, intriguing, simple and uncomplicated. We don't want it overly busy, technical, or complex.
Nice to have
• MAYBE?? a broken heart being put back together.
Should not have
• No photo, no cartoon, no flowers, no couple (unless obscure and not gender specific).

```html
<!DOCTYPE html>
<html lang="en">
<head>
<meta charset="utf-8">
<title>Mend the Quiet Tide — Book Cover</title>
<link rel="stylesheet" href="https://fonts.googleapis.com/css2?family=Oswald:wght@600;700&family=Mrs+Saint+Delafield&family=Cinzel:wght@400;500&display=swap">
<style>
  :root {
    --page-bg: #e9e7e3;
    --cover-white: #ffffff;
    --teal-light: #55aebf;
    --teal-dark: #2b8799;
    --script-ink: #3a3a3c;
    --rule-grey: #cfcfcf;
    --subtitle-ink: #2d2d2f;
    --copper: #c58a52;
    --band-navy: #14232f;
    --band-text: #f4f1ea;
    --gold-hi: #f6d39a;
    --gold-mid: #d79a55;
    --gold-low: #9a5f2a;
  }
  * { box-sizing: border-box; margin: 0; padding: 0; }
  html, body {
    width: 1200px; height: 1200px; overflow: hidden;
    background: var(--page-bg);
  }
  .cover {
    position: absolute;
    left: 230px; top: 45px;
    width: 740px; height: 1110px;
    background: var(--cover-white);
    box-shadow: 0 8px 30px rgba(0,0,0,0.12);
    overflow: hidden;
  }
  .title {
    font-family: 'Oswald', sans-serif;
    font-weight: 700;
    text-transform: uppercase;
  }
  .title-line {
    position: absolute; left: 0; right: 0;
    text-align: center;
    white-space: nowrap;
    background: linear-gradient(180deg, var(--teal-light), var(--teal-dark));
    -webkit-background-clip: text; background-clip: text;
    color: transparent;
  }
  .title-line--first {
    top: 40px; font-size: 200px; line-height: 200px; letter-spacing: 6px;
  }
  .title-line--second {
    top: 290px; font-size: 138px; line-height: 138px; letter-spacing: 2px;
  }
  .title-script {
    position: absolute; left: 0; right: 0; top: 205px;
    text-align: center;
    font-family: 'Mrs Saint Delafield', cursive;
    font-size: 110px;
    line-height: 110px;
    color: var(--script-ink);
  }
  .title-rule {
    position: absolute; top: 268px; height: 2px; width: 200px;
    background: var(--rule-grey);
  }
  .title-rule--left { left: 70px; }
  .title-rule--right { right: 70px; }
  .rings {
    position: absolute; left: 250px; top: 470px;
    width: 240px; height: 210px;
    border-radius: 48% 48% 50% 50% / 55% 55% 45% 45%;
    background: radial-gradient(ellipse at 40% 35%, var(--gold-hi), var(--gold-mid) 55%, var(--gold-low));
  }
  .rings-shadow {
    position: absolute; left: 270px; top: 672px;
    width: 220px; height: 22px; border-radius: 50%;
    background: radial-gradient(ellipse, rgba(0,0,0,0.18), transparent 70%);
  }
  .subtitle {
    position: absolute; left: 0; right: 0; top: 730px;
    text-align: center;
    font-family: 'Cinzel', serif;
    font-weight: 500;
    font-size: 46px;
    line-height: 1.12;
    color: var(--subtitle-ink);
  }
  .subtitle-accent { color: var(--copper); }
  .author-band {
    position: absolute; left: 0; right: 0; bottom: 0; height: 130px;
    background: var(--band-navy);
    display: flex; align-items: center; justify-content: center;
  }
  .author-names {
    font-family: 'Cinzel', serif;
    font-weight: 500;
    font-size: 40px;
    letter-spacing: 1px;
    color: var(--band-text);
  }
</style>
</head>
<body>
  <main class="cover">
    <h1 class="title">
      <span class="title-line title-line--first">Mend</span>
      <span class="title-line title-line--second">Quiet Tide</span>
    </h1>
    <span class="title-rule title-rule--left"></span>
    <span class="title-rule title-rule--right"></span>
    <div class="title-script">the</div>

    <div class="rings" role="img" aria-label="Two interlocked gold wedding rings forming a heart shape"></div>
    <div class="rings-shadow"></div>

    <p class="subtitle">
      For partners<br>
      who <span class="subtitle-accent">still choose</span><br>
      to stay close
    </p>

    <footer class="author-band">
      <p class="author-names">Dennis &amp; Marla Holtwick</p>
    </footer>
  </main>
</body>
</html>
```